Valdorick Business Card Design

Valdorick is the holdings company for my portfolio of businesses. These businesses currently only include Valdorick Advising. V|A is a strategic consulting firm that focuses on small businesses and start-ups that want help with their brand. We focus on partnering with influencers (Pro Athletes and Celebrities) and Social Media Marketing. We also want to focus on companies that have a positive effect on the community or world. The audience I am going after is very corporate. I want to have the corporate edge with some 25yr old flair.
Industry/Entity Type
Business
Contact Information for Business Card
General Idea AttachedLogo (Attached)Jonathan R. MasonCEO & Managing MemberDown Left Bottom CornerPhone: 347-570-0585Cell: 240-604-7930mason@valdorick-example.comDown Right Bottom Corner 174 W 4th St, Ste 212New York, NY 10014www.valdorick-example.comBackside LogoI want the entire card extra thick and with metallic finish
Look and feel

```html
<!DOCTYPE html>
<html lang="en">
<head>
<meta charset="utf-8">
<title>Valdorick Holdings – Business Card</title>
<link href="https://fonts.googleapis.com/css2?family=Lato:wght@400;700;900&display=swap" rel="stylesheet">
<style>
  :root {
    --backdrop: #2b2b2d;
    --card: #ffffff;
    --card-shade: #f1f1f1;
    --brand-red: #a4121d;
    --brand-grey: #6b6b6d;
    --ink: #1e1e1e;
    --rule: #8a8a8a;
  }
  * { margin: 0; padding: 0; box-sizing: border-box; }
  html, body { width: 1200px; height: 873px; overflow: hidden; }
  body {
    background: var(--backdrop);
    font-family: "Lato", sans-serif;
    color: var(--ink);
    position: relative;
  }
  .card {
    position: absolute;
    top: 286px;
    width: 525px;
    height: 300px;
    background: linear-gradient(160deg, var(--card) 0%, var(--card-shade) 100%);
    box-shadow: 0 10px 30px rgba(0,0,0,.55);
    overflow: hidden;
  }
  .card--front { left: 50px; }
  .card--back { left: 625px; }
  .card__band { position: absolute; left: 0; bottom: 0; width: 525px; height: 22px; }

  .wordmark {
    position: absolute;
    display: flex;
    align-items: center;
    gap: 10px;
  }
  .wordmark__square {
    width: 40px; height: 40px;
    background: var(--brand-red);
  }
  .wordmark__name {
    font-weight: 700;
    color: var(--brand-red);
    letter-spacing: .04em;
    text-transform: uppercase;
    border-bottom: 1px solid var(--rule);
    padding-bottom: 4px;
  }
  .card--front .wordmark { left: 78px; top: 120px; }
  .card--front .wordmark__name { font-size: 27px; }
  .card--back .wordmark { left: 40px; top: 116px; }
  .card--back .wordmark__name { font-size: 22px; }

  .contact-person {
    position: absolute; right: 26px; top: 24px; text-align: right;
  }
  .contact-person__name { font-weight: 900; font-size: 16px; color: var(--brand-red); }
  .contact-person__title { font-size: 11px; margin-top: 2px; }

  .contact-list {
    position: absolute; right: 26px; list-style: none; text-align: right;
    font-size: 13px; line-height: 22px;
  }
  .contact-list--phones { top: 98px; }
  .contact-list--web { top: 196px; }
  .contact-list li { display: flex; justify-content: flex-end; align-items: center; gap: 6px; }
  .contact-list svg { width: 11px; height: 11px; fill: var(--brand-red); }

  .address {
    position: absolute; left: 30px; top: 222px;
    font-size: 14px; line-height: 22px; color: var(--brand-red);
  }
</style>
</head>
<body>

<section class="card card--front" aria-label="Card front">
  <div class="wordmark">
    <span class="wordmark__square"></span>
    <span class="wordmark__name">Valdorick Holdings LLC</span>
  </div>
  <svg class="card__band" viewBox="0 0 525 22" aria-hidden="true">
    <polygon points="0,8 420,0 412,22 0,22" fill="var(--brand-red)"/>
    <polygon points="428,0 525,0 525,22 420,22" fill="var(--brand-grey)"/>
  </svg>
</section>

<section class="card card--back" aria-label="Card back">
  <div class="contact-person">
    <div class="contact-person__name">Derrick L. Fanshaw</div>
    <div class="contact-person__title">CEO &amp; Managing Member</div>
  </div>

  <ul class="contact-list contact-list--phones">
    <li>347-555-0162
      <svg viewBox="0 0 12 12" aria-label="Office phone"><path d="M1 4c0-2 2-3 5-3s5 1 5 3l-2 1-1-2H4L3 5zM3 6h6l1 5H2z"/></svg>
    </li>
    <li>240-555-0187
      <svg viewBox="0 0 12 12" aria-label="Mobile phone"><path d="M3 0h6a1 1 0 0 1 1 1v10a1 1 0 0 1-1 1H3a1 1 0 0 1-1-1V1a1 1 0 0 1 1-1zm0 2v7h6V2z"/></svg>
    </li>
  </ul>

  <ul class="contact-list contact-list--web">
    <li>fanshaw@valdorick-example.com
      <svg viewBox="0 0 12 12" aria-label="Email"><path d="M0 2h12v8H0zm1 1 5 4 5-4z" fill-rule="evenodd"/></svg>
    </li>
    <li>www.valdorick-example.com
      <svg viewBox="0 0 12 12" aria-label="Website"><path d="M5 7 7 5M4 6 2 8a1.5 1.5 0 0 0 2 2l2-2M8 6l2-2a1.5 1.5 0 0 0-2-2L6 4" stroke="var(--brand-red)" stroke-width="1.6" fill="none"/></svg>
    </li>
  </ul>

  <div class="wordmark">
    <span class="wordmark__name">Valdorick Holdings LLC</span>
  </div>

  <address class="address" style="font-style:normal">
    88 E 9th St, Ste 405<br>New York, NY 10099
  </address>

  <svg class="card__band" viewBox="0 0 525 22" aria-hidden="true">
    <polygon points="0,10 420,0 412,22 0,22" fill="var(--brand-red)"/>
    <polygon points="428,0 525,0 525,22 420,22" fill="var(--brand-grey)"/>
  </svg>
</section>

</body>
</html>
```